"Harrow Crest Builders" is a residential building company and needs a new business card design and may re

We would like a redesign based on the existing logo, and would like to see a new font as well. We are bespoke home builders who build sustainable energy efficient homes.

Industry/Entity Type

Construction

Contact Information for Business Card

Business card size 40mm x 90mm

Colors

Designer to choose colors to be used in the design.

```html
<!DOCTYPE html>
<html lang="en">
<head>
<meta charset="utf-8">
<title>Harrow Crest Builders – Business Card</title>
<link rel="stylesheet" href="https://fonts.googleapis.com/css2?family=Inter:wght@400;500;700&display=swap">
<style>
  :root {
    --page: #e4e2df;
    --card: #f9f9f7;
    --ink: #161616;
    --yellow: #f2cf2a;
    --pattern-a: #9a9a98;
    --pattern-b: #d2d2d0;
  }
  * { margin: 0; padding: 0; box-sizing: border-box; }
  html, body {
    width: 1200px; height: 1200px; overflow: hidden;
    background: var(--page);
    font-family: "Inter", Arial, sans-serif;
    color: var(--ink);
  }
  .stage {
    position: relative; width: 1200px; height: 1200px;
    display: flex; align-items: center; justify-content: center; gap: 100px;
  }
  .card {
    position: relative; width: 400px; height: 640px;
    background: var(--card);
    box-shadow: 0 0 0 3px var(--yellow), 0 10px 30px rgba(0,0,0,.12);
    overflow: hidden;
  }

  /* Front */
  .card-front__pattern {
    position: absolute; inset: 0;
    background: linear-gradient(160deg, var(--pattern-a), var(--pattern-b) 50%, var(--pattern-a));
  }
  .card-front__frame {
    position: absolute; left: 60px; top: 120px; width: 280px; height: 400px;
    background: var(--card);
    border: 8px solid var(--ink);
    display: flex; align-items: center; justify-content: center;
  }
  .brand {
    writing-mode: vertical-rl;
    display: flex; align-items: center; gap: 18px;
    color: var(--yellow);
    font-weight: 700; font-size: 40px; line-height: 1; letter-spacing: -0.5px;
  }
  .brand__mark {
    width: 64px; height: 64px; background: var(--yellow);
  }

  /* Back */
  .card-back__company {
    position: absolute; left: 40px; top: 40px;
    font-size: 17px; font-weight: 400;
  }
  .card-back__block {
    position: absolute; left: 95px; top: 190px; width: 210px; height: 210px;
    background: var(--yellow);
  }
  .card-back__contact {
    position: absolute; left: 170px; top: 160px;
    writing-mode: vertical-rl;
    line-height: 1.05;
  }
  .contact__name { font-size: 31px; font-weight: 700; }
  .contact__phone { font-size: 31px; font-weight: 400; }
  .card-back__email {
    position: absolute; left: 46px; top: 190px;
    writing-mode: vertical-rl;
    font-size: 16px;
  }
  .card-back__legal {
    position: absolute; right: 30px; top: 320px;
    writing-mode: vertical-rl;
    font-size: 13px;
  }
</style>
</head>
<body>
<main class="stage">
  <section class="card card-front">
    <div class="card-front__pattern" role="img" aria-label="Repeating black brand pattern across the card"></div>
    <div class="card-front__frame">
      <div class="brand">
        <span class="brand__mark"></span>
        <span class="brand__name">Harrow Crest Builders</span>
      </div>
    </div>
  </section>

  <section class="card card-back">
    <p class="card-back__company">Harrow Crest Builders Pty Ltd</p>
    <div class="card-back__block"></div>
    <div class="card-back__contact">
      <p class="contact__name">Daniel Prescott</p>
      <p class="contact__phone">0400 555 318</p>
    </div>
    <p class="card-back__email">daniel@harrowcrestbuilders.com.au</p>
    <p class="card-back__legal">Registration 40518 ABN: 12 345 678 901</p>
  </section>
</main>
</body>
</html>
```